Ledgerwise Reach - B2B Demand Generation Website Project

We need a fully functional website for www.ledgerwisereach.example. We are a B2B Demand Generation company, based in London, working with companies such as QRT, VKD, Norvex, Brindlow, Tarvo generating them sales leads for their sales teams. We run this through digital marketing newsletter promotions and have a network of websites. Content syndication, data, demand generation, online marketing. Our logo has just been redone (attached) and we have a holding page already which i would like to use the style / colours. Our logo is bright and vibrant but i dont want the site to be a rainbow. We are expensive, classy, professorial, B2B, intelligent.

Home
About Us
Our Services
Prospora & QA Technology
Intent Data
Testimonials
Contact Us
Updates

Target Market(s)

B2B Marketers (QRT, Velquarion, Tarvo, VKD, Opal Reach, Driftmoor, Harlow Quantis, Technology Companies, Data Companies, Marketing Teams, Tumbleden.

Industry/Entity Type

Marketing

Coding

Coded - Design and coding required

Number of Pages Required

5+ page

Font styles to use
Sans Serif

Requirements
Must have
• Home
About Us
Our Services
Prospora & QA Technology
Intent Data
Testimonials
Contact Us

Simple Pages.

Look classy, intelligent, data experts. I like the video homepages were the image moves at the top. Very soft animation.
Nice to have
• Websites i like:

https://www.vkd.example/
https://www.brevantor.example/
https://www.plumfieldsites.example.co.uk/

Ledgerwise Reach - The Demand Generation Company
Should not have
• Glimpsevault crap images

```html
<!DOCTYPE html>
<html lang="en">
<head>
<meta charset="utf-8">
<title>Ledgerwise Reach - The Demand Generation Company</title>
<link rel="stylesheet" href="https://fonts.googleapis.com/css2?family=Poppins:wght@300;400;500;600;700&family=Oswald:wght@500&display=swap">
<style>
:root{
  --red:#c8242b;
  --red-dark:#a81a21;
  --navy:#12408a;
  --navy-deep:#0c3a80;
  --ink:#2e3340;
  --muted:#6b7280;
  --pale:#eef3fa;
  --pale-blue:#f3f7fc;
  --pale-red:#fbeeee;
  --line:#e3e7ee;
  --art-1:#dce7f7;
  --art-2:#b9cdec;
  --art-3:#f3d6d8;
}
*{box-sizing:border-box;margin:0;padding:0}
html,body{width:1200px;height:4057px;overflow:hidden;background:#fff}
body{font-family:'Poppins',sans-serif;color:var(--ink)}
.page{position:relative;width:1200px;height:4057px;overflow:hidden}
.abs{position:absolute}
a{text-decoration:none;color:inherit}

/* header */
.phone-tab{position:absolute;left:913px;top:0;width:174px;height:28px;background:var(--red);color:#fff;font-size:11px;font-weight:500;display:flex;align-items:center;justify-content:center;gap:8px;border-radius:0 0 0 18px}
.phone-tab::after{content:"";position:absolute;right:-113px;top:0;width:113px;height:3px;background:var(--red)}
.brand{position:absolute;left:108px;top:14px;display:flex;flex-direction:column;align-items:center}
.brand-mark{width:32px;height:32px;border-radius:50%;background:var(--red);margin-bottom:5px}
.brand-name{font-size:19px;font-weight:400;color:var(--red);line-height:1}
.brand-tag{font-size:6px;color:var(--navy);margin-top:3px;letter-spacing:.2px}
.nav{position:absolute;top:50px;right:110px;display:flex;gap:28px;font-size:12.5px;font-weight:400;color:var(--navy)}
.nav .active{color:var(--red)}

/* generic */
.heading{font-weight:400;line-height:1.08;font-size:46px}
.heading .r{color:var(--red);display:block}
.heading .b{color:var(--navy);display:block}
.body-copy{font-size:11px;line-height:24px;color:var(--ink)}
.btn{position:absolute;height:40px;border:2px solid var(--navy);border-radius:20px;color:var(--red);font-size:10px;font-weight:600;display:flex;align-items:center;justify-content:center;letter-spacing:.4px;background:#fff}
.btn::after{content:"";position:absolute;right:22px;bottom:-9px;width:12px;height:12px;background:#fff;border-right:2px solid var(--navy);border-bottom:2px solid var(--navy);transform:skewX(30deg) rotate(20deg)}
.art{position:absolute;border-radius:28px;background:linear-gradient(150deg,var(--art-1) 0%,var(--art-2) 62%,var(--art-3) 100%)}

/* partners */
.partners-line{position:absolute;left:107px;width:983px;height:1px;background:var(--line)}
.partners-title{position:absolute;left:0;width:1200px;top:637px;text-align:center;font-size:12.5px;color:var(--navy);font-weight:500}
.partners-title span{background:#fff;padding:0 14px}
.partners{position:absolute;left:107px;top:692px;width:983px;display:flex;justify-content:space-between;align-items:center}
.partners span{font-size:19px;font-weight:600;color:#5b6f93}

/* services */
.blob{position:absolute;background:var(--pale);border-radius:50%}
.svc-card{position:absolute;background:#fff;box-shadow:0 6px 24px rgba(18,64,138,.08);text-align:center;padding:0 18px}
.svc-icon{width:64px;height:64px;border-radius:50%;background:var(--pale-red);margin:24px auto 18px;display:flex;align-items:center;justify-content:center}
.svc-title{font-size:15px;color:var(--navy);font-weight:400;line-height:19px}
.svc-text{font-size:9.5px;line-height:18px;color:var(--muted);margin-top:8px}
.svc-arrow{display:block;margin:12px auto 0;width:24px}
.svc-card.featured{background:var(--red);box-shadow:0 10px 30px rgba(200,36,43,.25)}
.svc-card.featured .svc-icon{background:rgba(255,255,255,.18)}
.svc-card.featured .svc-title,.svc-card.featured .svc-text{color:#fff}

/* about */
.center{text-align:center}
.about-copy{position:absolute;left:245px;width:710px;top:1617px;font-size:10.5px;line-height:18px;text-align:center;color:var(--ink)}
.about-copy p{margin-bottom:14px}
.feature{position:absolute;top:1858px;width:174px;height:130px;font-size:10.5px;line-height:17px;text-align:center;display:flex;flex-direction:column;align-items:center;padding-top:30px;border:1px solid #e6ebf2}
.feature.blue{background:var(--pale-blue)}
.feature.red{background:var(--pale-red)}
.num{width:18px;height:18px;border-radius:50%;color:#fff;font-size:9px;font-weight:600;display:flex;align-items:center;justify-content:center;margin-bottom:14px}
.num.r{background:var(--red)}
.num.b{background:var(--navy)}

/* stats */
.stat{position:absolute;top:3024px;width:200px;text-align:center}
.stat-label{font-size:10.5px;color:var(--navy)}
.stat-num{font-family:'Oswald',sans-serif;font-weight:500;font-size:38px;color:var(--red);line-height:46px}
.stat-pill{display:inline-block;margin-top:6px;padding:5px 24px;border-radius:14px;background:var(--pale);font-size:10.5px;font-weight:500;color:var(--navy)}

/* testimonials */
.quote{position:absolute;top:3303px;width:370px;height:123px;padding:20px 26px 0 24px;font-size:9.5px;line-height:21px;color:var(--muted)}
.quote.blue{background:var(--pale-blue)}
.quote.red{background:var(--pale-red)}
.quote-mark{position:absolute;left:14px;top:-20px;font-size:74px;font-weight:700;color:var(--red);line-height:1}
.quote.blue .quote-mark{color:var(--navy)}
.quote p{padding-left:32px}
.author{position:absolute;top:3437px;display:flex;align-items:center;gap:12px}
.avatar{width:56px;height:56px;border-radius:50%;background:#cfd8e6;border:3px solid #fff;box-shadow:0 0 0 2px var(--pale-red)}
.author-name{font-size:11.5px;color:var(--navy);font-weight:500}
.author-name small{color:var(--red);font-size:9.5px;font-weight:400;margin-left:6px}
.stars{color:#f5a623;font-size:10px;letter-spacing:1px}
.chev{position:absolute;top:3350px}

/* cta */
.cta{position:absolute;left:150px;top:3591px;width:1050px;height:126px;background:var(--navy-deep);border-radius:63px 0 0 63px}
.cta-tail{position:absolute;left:210px;top:3690px}
.cta-text{position:absolute;left:225px;top:3628px;font-size:34px;font-weight:300;color:#fff}
.cta-btn{position:absolute;left:830px;top:3635px;width:160px;height:35px;border-radius:18px;background:#fff;color:var(--navy);font-size:10px;font-weight:600;display:flex;align-items:center;justify-content:center}
.chat{position:absolute;left:1057px;top:3677px;width:66px;height:66px;border-radius:50%;background:var(--red);border:5px solid #f4c8ca;display:flex;align-items:center;justify-content:center}

/* footer */
.f-title{position:absolute;top:3786px;font-size:20px;font-weight:400;color:var(--red)}
.f-title .b{color:var(--navy)}
.f-row{position:absolute;display:flex;gap:14px;font-size:10.5px;line-height:16px;color:var(--ink);align-items:flex-start}
.f-links{position:absolute;left:636px;top:3826px;font-size:10px;line-height:26px;color:var(--ink);list-style:none}
.f-links li::before{content:"› ";color:var(--red)}
.social{position:absolute;top:3888px;width:28px;height:28px;border-radius:50%}
.input{position:absolute;left:792px;top:3827px;width:197px;height:30px;border:1px solid var(--line);border-radius:15px;font-size:10px;color:var(--muted);padding:7px 18px}
.subscribe{position:absolute;left:792px;top:3868px;width:197px;height:33px;border-radius:17px;background:var(--red);color:#fff;font-size:10px;font-weight:600;display:flex;align-items:center;justify-content:center}
.copyright{position:absolute;top:4026px;left:0;width:1200px;text-align:center;font-size:10px;color:var(--muted)}
</style>
</head>
<body>
<div class="page">

  <!-- header -->
  <div class="phone-tab">
    <svg width="13" height="13" viewBox="0 0 24 24" fill="none" stroke="#fff" stroke-width="2"><path d="M22 16.9v3a2 2 0 0 1-2.2 2 19.8 19.8 0 0 1-8.6-3.1 19.5 19.5 0 0 1-6-6A19.8 19.8 0 0 1 2.1 4.2 2 2 0 0 1 4.1 2h3a2 2 0 0 1 2 1.7c.1 1 .4 1.9.7 2.8a2 2 0 0 1-.5 2.1L8 9.9a16 16 0 0 0 6 6l1.3-1.3a2 2 0 0 1 2.1-.4c.9.3 1.8.6 2.8.7a2 2 0 0 1 1.7 2z"/></svg>
    +01-555-01890
  </div>
  <a class="brand" href="#">
    <span class="brand-mark"></span>
    <span class="brand-name">ledgerwise reach</span>
    <span class="brand-tag">The Demand Generation Company</span>
  </a>
  <nav class="nav">
    <a class="active" href="#">home</a>
    <a href="#">about us</a>
    <a href="#">our services</a>
    <a href="#">prospora &amp; QA Technology</a>
    <a href="#">Intent Data</a>
    <a href="#">Testimonials</a>
    <a href="#">Contact us</a>
  </nav>

  <!-- hero -->
  <h1 class="heading abs" style="left:108px;top:200px"><span class="r">we generate the</span><span class="b">demand</span></h1>
  <p class="body-copy abs" style="left:110px;top:318px;width:410px">Ledgerwise Reach offers multi-channel demand generation services to publishers and technology vendors through our network of lead generation websites and native speaking telemarketing agents.</p>
  <a class="btn" href="#" style="left:110px;top:406px;width:153px">LET'S WORK NOW!</a>
  <div class="art" role="img" aria-label="Isometric illustration of a data platform with charts, servers and people analysing leads" style="left:590px;top:105px;width:500px;height:470px"></div>

  <!-- partners -->
  <div class="partners-line" style="top:646px"></div>
  <div class="partners-title"><span>who we work with</span></div>
  <div class="partners">
    <span>Caldrex</span><span>Ormwell</span><span>QRT</span><span>Tarvo</span><span>VKD</span><span>Quillon</span><span>Saltmere</span><span>Weekhaven</span><span>Cindral</span>
  </div>
  <div class="partners-line" style="top:756px"></div>

  <!-- services -->
  <div class="blob" style="left:-140px;top:860px;width:560px;height:620px;border-radius:48% 52% 55% 45%"></div>
  <div class="blob" style="left:300px;top:960px;width:360px;height:340px"></div>
  <div class="svc-card" style="left:110px;top:843px;width:229px;height:283px">
    <div class="svc-icon"><svg width="26" height="26" viewBox="0 0 24 24" fill="none" stroke="#c8242b" stroke-width="1.8"><path d="M4 4v16h16"/><path d="M8 15l4-4 3 3 5-6"/></svg></div>
    <div class="svc-title">marketing<br>qualified leads</div>
    <div class="svc-text">A Marketing Qualified Lead (MQL) is a prospect that has expressed an interest in what your brand has to offer. An MQL has taken...</div>
    <svg class="svc-arrow" height="12" viewBox="0 0 24 12" fill="none" stroke="#c8242b" stroke-width="1.4"><path d="M0 6h22M17 1l5 5-5 5"/></svg>
  </div>
  <div class="svc-card featured" style="left:373px;top:987px;width:225px;height:281px">
    <div class="svc-icon"><svg width="26" height="26" viewBox="0 0 24 24" fill="none" stroke="#fff" stroke-width="1.8"><circle cx="12" cy="12" r="8"/><circle cx="12" cy="12" r="3"/></svg></div>
    <div class="svc-title">Account Based<br>Marketing Leads</div>
    <div class="svc-text">ABM is a strategy that directs marketing resources to engaging a specific set of target accounts. Instead of casting a wide ...</div>
    <svg class="svc-arrow" height="12" viewBox="0 0 24 12" fill="none" stroke="#fff" stroke-width="1.4"><path d="M0 6h22M17 1l5 5-5 5"/></svg>
  </div>
  <div class="svc-card" style="left:110px;top:1165px;width:229px;height:284px">
    <div class="svc-icon"><svg width="26" height="26" viewBox="0 0 24 24" fill="none" stroke="#c8242b" stroke-width="1.8"><path d="M5 20V13M10 20V9M15 20V11M20 20V5"/></svg></div>
    <div class="svc-title">Sales Qualified<br>Lead / BANT</div>
    <div class="svc-text">An SQL lead or a BANT lead is a type of lead that expressed a specific interest in a product and service that you have to offer...</div>
    <svg class="svc-arrow" height="12" viewBox="0 0 24 12" fill="none" stroke="#c8242b" stroke-width="1.4"><path d="M0 6h22M17 1l5 5-5 5"/></svg>
  </div>
  <h2 class="heading abs" style="left:697px;top:1032px"><span class="r">our</span><span class="b">services</span></h2>
  <p class="body-copy abs" style="left:700px;top:1144px;width:390px;font-size:10.5px;line-height:26px">Whether looking for MQL, ABM or BANT campaigns, Ledgerwise Reach can assist you in delivering your demand generation strategy and generate pipeline for your sales teams and/or channel partners.</p>

  <!-- about -->
  <div class="abs" style="left:580px;top:1512px;width:40px;height:40px;border-radius:50%;background:var(--red)"></div>
  <h2 class="abs center" style="left:0;width:1200px;top:1555px;font-size:36px;font-weight:400;color:var(--red)">about us</h2>
  <div class="about-copy">
    <p>Ledgerwise Reach can deliver high quality sales leads from any country in the world. This can include leads via email or telemarketing, account-based targeting (ABM) or identifying need and pain points through BANT / SQL campaigns</p>
    <p>Ledgerwise Reach offer expert demand generation support, from providing detailed leads of qualified decision-makers, to a comprehensive lead generation and SQL service.</p>
    <p>Our extensive and ongoing research campaigns give you the ability to build contact lists that identify individuals at all stages of the buying cycle, from pre-sales to sales ready.</p>
    <p>With access to over 31 million names, Ledgerwise Reach offers a range of marketing options that allow you to use our data to target the decision makers you need to reach.</p>
  </div>
  <div class="abs center" style="left:0;width:1200px;top:1822px;font-size:12px;color:var(--ink)">this can include</div>
  <div class="feature blue" style="left:209px"><span class="num r">1</span>Breakdown by<br>geography, job title, role<br>and responsibility</div>
  <div class="feature red" style="left:413px"><span class="num b">2</span><br>Email dispatch to<br>selected individuals</div>
  <div class="feature blue" style="left:614px"><span class="num r">3</span>Targeting through<br>previous research and<br>buying intention</div>
  <div class="feature red" style="left:816px"><span class="num b">4</span><br>Extensive<br>telemarketing options</div>

  <!-- prospora -->
  <h2 class="heading abs" style="left:107px;top:2088px;font-size:42px"><span class="r">prospora &amp;</span><span class="b">QA Technology</span></h2>
  <p class="body-copy abs" style="left:110px;top:2196px;width:400px;font-size:10.5px;line-height:26px">Prospora is a proprietary lead verification platform from Ledgerwise Reach that aims to sift out invalid leads with questionable or erroneous data. The platform is designed to equip sales teams with accurate, high-quality records in order to improve lead generation, accelerate pipeline and increase revenue.</p>
  <a class="btn" href="#" style="left:110px;top:2343px;width:127px">LEARN MORE</a>
  <div class="art" role="img" aria-label="Isometric illustration of a laptop with lead verification charts and dashboards" style="left:600px;top:2060px;width:490px;height:365px"></div>

  <!-- intent -->
  <div class="art" role="img" aria-label="Isometric illustration of a data server connected to storage nodes" style="left:105px;top:2530px;width:450px;height:420px"></div>
  <h2 class="heading abs" style="left:619px;top:2565px;font-size:42px"><span class="r">intent</span><span class="b">Data works</span></h2>
  <p class="body-copy abs" style="left:621px;top:2664px;width:468px;font-size:10.5px;line-height:26px">Our relationships with the world's most important technology &amp; business decisions-makers generate a perpetual stream of global data. With access to 35 million individuals and a global behavioural data stream that is authenticated, timely and contextually relevant, we have one of the industry's most powerful signals of buyer intent and can fuel your demand-generation marketing strategies globally.</p>
  <a class="btn" href="#" style="left:621px;top:2819px;width:127px">LEARN MORE</a>

  <!-- stats -->
  <div class="stat" style="left:231px"><div class="stat-label">ticker to</div><div class="stat-num">70,000+</div><div class="stat-pill">downloads per month</div></div>
  <div class="stat" style="left:500px"><div class="stat-label">ticker to</div><div class="stat-num">25,000+</div><div class="stat-pill">Leads Delivered per month</div></div>
  <div class="stat" style="left:769px"><div class="stat-label">ticker to</div><div class="stat-num">50+</div><div class="stat-pill">Countries We Can Reach</div></div>
  <div class="partners-line" style="top:3153px"></div>

  <!-- testimonials -->
  <h2 class="abs center" style="left:0;width:1200px;top:3230px;font-size:36px;font-weight:400;color:var(--red)">our <span style="color:var(--navy)">testimonails</span></h2>
  <svg class="chev" style="left:160px" width="20" height="40" viewBox="0 0 20 40" fill="none" stroke="#c9d2e0" stroke-width="1.5"><path d="M18 2L2 20l16 18"/></svg>
  <svg class="chev" style="left:1020px" width="20" height="40" viewBox="0 0 20 40" fill="none" stroke="#c9d2e0" stroke-width="1.5"><path d="M2 2l16 18L2 38"/></svg>
  <div class="quote blue" style="left:211px"><span class="quote-mark">&ldquo;</span><p>Lorem ipsum dolor sit amet, consectetur adipiscing elit. Sed etosigs laoreet orcu. Pellentesque habitant morbi tristique senectus et lose netus et malesuada fames ac turpis egestas. Donec sapien miasi ti tempus quis ex id, blandit iaculis orci.</p></div>
  <div class="quote red" style="left:619px"><span class="quote-mark">&ldquo;</span><p>Lorem ipsum dolor sit amet, consectetur adipiscing elit. Sed etosigs laoreet orcu. Pellentesque habitant morbi tristique senectus et lose netus et malesuada fames ac turpis egestas. Donec sapien miasi ti tempus quis ex id, blandit iaculis orci.</p></div>
  <div class="author" style="left:215px"><div class="avatar" role="img" aria-label="Portrait photo of the client"></div><div><div class="author-name">Tomas Reyland<small>( Saltmere )</small></div><div class="stars">★★★★★</div></div></div>
  <div class="author" style="left:623px"><div class="avatar" role="img" aria-label="Portrait photo of the client"></div><div><div class="author-name">Ines Corwell<small>( Weekhaven )</small></div><div class="stars">★★★★★</div></div></div>

  <!-- call to action -->
  <div class="cta"></div>
  <svg class="cta-tail" width="70" height="60" viewBox="0 0 70 60"><path d="M0 0h70L2 58z" fill="#0c3a80"/></svg>
  <div class="cta-text">let's generate demand!</div>
  <a class="cta-btn" href="#">LET'S WORK NOW!</a>
  <div class="chat">
    <svg width="26" height="26" viewBox="0 0 24 24" fill="none" stroke="#fff" stroke-width="2"><path d="M21 12a8 8 0 0 1-11.6 7.1L4 20l1-4.6A8 8 0 1 1 21 12z"/><circle cx="8.5" cy="12" r=".6" fill="#fff"/><circle cx="12" cy="12" r=".6" fill="#fff"/><circle cx="15.5" cy="12" r=".6" fill="#fff"/></svg>
  </div>

  <!-- footer -->
  <div class="brand" style="left:210px;top:3792px">
    <span class="brand-mark" style="width:40px;height:40px"></span>
    <span class="brand-name" style="font-size:22px">ledgerwise reach</span>
    <span class="brand-tag">The Demand Generation Company</span>
  </div>
  <span class="social" style="left:238px;background:#1f5fbf" role="img" aria-label="Social profile"></span>
  <span class="social" style="left:276px;background:#2d8fe0" role="img" aria-label="Social profile"></span>
  <span class="social" style="left:314px;background:#e0442e" role="img" aria-label="Social profile"></span>

  <h3 class="f-title" style="left:419px">contact <span class="b">us</span></h3>
  <div class="f-row" style="left:419px;top:3832px">
    <svg width="18" height="20" viewBox="0 0 24 24" fill="none" stroke="#12408a" stroke-width="1.6"><path d="M12 22s7-6.5 7-12a7 7 0 0 0-14 0c0 5.5 7 12 7 12z"/><circle cx="12" cy="10" r="2.5"/></svg>
    <span style="font-size:9.5px">51 Harbour Row, Ledgerwise<br>Reach LN-24567</span>
  </div>
  <div class="f-row" style="left:419px;top:3882px">
    <svg width="18" height="18" viewBox="0 0 24 24" fill="none" stroke="#12408a" stroke-width="1.6"><path d="M22 16.9v3a2 2 0 0 1-2.2 2 19.8 19.8 0 0 1-8.6-3.1 19.5 19.5 0 0 1-6-6A19.8 19.8 0 0 1 2.1 4.2 2 2 0 0 1 4.1 2h3a2 2 0 0 1 2 1.7c.1 1 .4 1.9.7 2.8a2 2 0 0 1-.5 2.1L8 9.9a16 16 0 0 0 6 6l1.3-1.3a2 2 0 0 1 2.1-.4c.9.3 1.8.6 2.8.7a2 2 0 0 1 1.7 2z"/></svg>
    <span>+01-555-01890</span>
  </div>
  <div class="f-row" style="left:419px;top:3918px">
    <svg width="18" height="16" viewBox="0 0 24 20" fill="none" stroke="#12408a" stroke-width="1.6"><rect x="2" y="2" width="20" height="16" rx="2"/><path d="M2 4l10 7 10-7"/></svg>
    <span style="font-size:9.5px">info@ledgerwisereach.example</span>
  </div>

  <h3 class="f-title" style="left:636px;color:var(--navy)">quick <span style="color:var(--red)">links</span></h3>
  <ul class="f-links">
    <li>about us</li><li>our services</li><li>Testimonials</li><li>Privacy Policy</li><li>Contact us</li>
  </ul>

  <h3 class="f-title" style="left:791px">our <span class="b">newsletter</span></h3>
  <div class="input">enter mail...</div>
  <div class="subscribe">SUBSCRIBE</div>

  <div class="copyright">©2020 ledgerwisereach.example, all rights reserved</div>
</div>
</body>
</html>
```